Website for AV installation with booking system and e-commerce

Company: Velqora
Tag Line: Audio Visual and Security System Installations
We need a website for an AV company based in Sydney Australia. We specialise in Audio Visual, CCTV (security cameras), and Data Cabling.
The purpose of the website is that customers book their installation online with a live booking system.
We are looking for the following:
- Creative and modern design
- easy to use - keep in mind that the user who will book will have little knowledge in technology.
- clean and organised
- colours to work in well with our logo we also like royal to navy blue, but we are open to other suggested what works well with our logo.
We want customers to be able to add products needed for their installation ie when booking to wall mount their TV they can choose to add a TV bracket and cables to the cart and vise-versa buy a bracket or cables and add to cart the installation.
Tabs to be included:
About us
Gallery
Contact Us
Home
Services (there are three services that we offer - Residential, Corporate and Retail)
Products
Book Online/Cart (checkout)
Temporary website checkout: www.velqora.com.au, please note this is very basic and we do not want a copy of this. This is purely to give you an idea of our company.
Good Luck!
Updates
Target Market(s)
home owners/renters, business owners, archiects/designers, builders
Industry/Entity Type
E-Commerce
Look and feel

```html
<!DOCTYPE html>
<html lang="en">
<head>
<meta charset="utf-8">
<title>Velqora — Audio Visual &amp; Security System Installations</title>
<link rel="stylesheet" href="https://fonts.googleapis.com/css2?family=Bebas+Neue&family=Lora:ital,wght@1,400&family=Montserrat:wght@400;600;700&family=Open+Sans:wght@400;600&display=swap">
<style>
  :root {
    --black: #000;
    --ink: #1c1c1c;
    --text: #555;
    --muted: #777;
    --white: #fff;
    --red: #e3313c;
    --green: #5cbf3a;
    --band: #ececec;
    --quote-band: #f2f2f2;
    --footer: #3a3a3a;
    --fb: #3b5a9a;
    --tw: #3fa9e0;
  }
  * { box-sizing: border-box; margin: 0; padding: 0; }
  html, body { width: 896px; height: 1200px; overflow: hidden; }
  body { position: relative; background: var(--white); font-family: "Open Sans", sans-serif; color: var(--text); }
  .abs { position: absolute; }

  /* Header */
  .site-header { position: absolute; left: 0; top: 0; width: 896px; height: 457px; background: var(--black); overflow: hidden; }
  .header-glow { position: absolute; inset: 0; }
  .brand { left: 105px; top: 28px; display: flex; align-items: center; gap: 8px; font-family: "Montserrat", sans-serif; font-weight: 700; font-size: 30px; color: var(--red); letter-spacing: -0.5px; }
  .brand-dot { width: 14px; height: 14px; background: var(--red); border-radius: 50%; }
  .contact-line { right: 106px; top: 26px; text-align: right; color: var(--white); }
  .contact-line em { display: block; font-family: "Lora", serif; font-size: 14px; color: #ccc; }
  .contact-line strong { display: block; font-family: "Montserrat", sans-serif; font-weight: 400; font-size: 23px; letter-spacing: 0.5px; line-height: 26px; }

  .main-nav { left: 140px; top: 89px; display: flex; }
  .main-nav a { display: block; width: 103px; height: 26px; transform: skewX(-30deg); background: linear-gradient(#b4ef8a, var(--green) 55%, #3e9a24); text-decoration: none; border-right: 1px solid #2f7a1a; }
  .main-nav a span { display: block; transform: skewX(30deg); text-align: center; line-height: 26px; font-family: "Montserrat", sans-serif; font-weight: 600; font-size: 13px; color: #111; letter-spacing: 0.3px; }

  .hero { left: 105px; top: 136px; width: 686px; height: 301px; background: var(--white); border-radius: 4px; padding: 6px; }
  .hero-inner { position: relative; width: 100%; height: 100%; background: #000; overflow: hidden; }
  .hero-photo { position: absolute; left: 0; top: 0; width: 460px; height: 100%; background: linear-gradient(90deg, rgba(0,0,0,0) 60%, #000 100%), linear-gradient(180deg, #1f2627 0%, #4c5a5c 55%, #8b9596 100%); }
  .hero-title { position: absolute; right: 32px; top: 48px; text-align: right; font-family: "Montserrat", sans-serif; font-weight: 600; font-size: 23.5px; line-height: 29px; color: var(--white); }
  .hero-copy { position: absolute; right: 32px; top: 126px; width: 285px; text-align: right; font-size: 10.3px; line-height: 16px; color: #bbb; }
  .hero-dots { position: absolute; right: 32px; bottom: 24px; display: flex; gap: 3px; }
  .hero-dots i { width: 5px; height: 5px; background: #777; }
  .hero-dots i:first-child { background: var(--white); }

  /* Services */
  .services-band { left: 0; top: 457px; width: 896px; height: 179px; background: linear-gradient(#fff, var(--band)); }
  .service-card { top: 475px; width: 211px; height: 141px; background: var(--white); box-shadow: 0 1px 4px rgba(0,0,0,0.25); padding: 4px; }
  .service-photo { width: 100%; height: 133px; }
  .service-label { position: absolute; left: 4px; bottom: 4px; height: 31px; padding: 0 32px 0 9px; background: #1a1a1a; color: var(--white); font-family: "Montserrat", sans-serif; font-weight: 600; font-size: 16px; line-height: 31px; clip-path: polygon(0 0, 88% 0, 100% 100%, 0 100%); }

  /* Welcome */
  .welcome-title { left: 105px; top: 652px; width: 686px; display: flex; align-items: center; gap: 12px; }
  .welcome-title::before, .welcome-title::after { content: ""; flex: 1; height: 2px; background: #e2e2e2; }
  .welcome-title h2 { font-family: "Lora", serif; font-style: italic; font-weight: 400; font-size: 21px; color: #555; }
  .welcome-title h2 b { font-family: "Montserrat", sans-serif; font-style: normal; font-weight: 700; color: var(--red); font-size: 21px; }
  .welcome-copy { left: 108px; top: 698px; width: 680px; text-align: center; font-size: 9.9px; line-height: 16px; color: #555; }
  .welcome-copy p + p { margin-top: 16px; }

  /* Accessories */
  .accessories { left: 105px; top: 838px; width: 250px; }
  .accessories h3 { font-family: "Montserrat", sans-serif; font-weight: 400; font-size: 20px; color: var(--ink); line-height: 24px; letter-spacing: 0.3px; }
  .accessories h2 { font-family: "Bebas Neue", sans-serif; font-weight: 400; font-size: 57px; line-height: 50px; color: var(--red); letter-spacing: 1px; }
  .accessories p { margin-top: 8px; width: 225px; font-size: 9.6px; line-height: 15.5px; color: #444; }
  .btn { display: block; text-align: center; text-decoration: none; color: var(--white); font-family: "Montserrat", sans-serif; font-weight: 600; border-radius: 3px; }
  .btn-shop { left: 218px; top: 1022px; width: 124px; height: 29px; line-height: 29px; font-size: 16px; background: linear-gradient(#7dd055, #4eaa2d); }
  .cables-photo { left: 345px; top: 828px; width: 180px; height: 258px; opacity: 0.7; }
  .divider { left: 523px; top: 830px; width: 6px; height: 250px; background: linear-gradient(90deg, rgba(0,0,0,0.08), rgba(0,0,0,0)); }

  /* Booking */
  .booking { left: 560px; top: 834px; width: 230px; }
  .booking h2 { font-family: "Bebas Neue", sans-serif; font-weight: 400; font-size: 56px; line-height: 56px; color: var(--red); letter-spacing: 0.3px; }
  .booking-options { list-style: none; margin-top: 3px; }
  .booking-options li { display: flex; align-items: center; gap: 7px; height: 22.5px; font-size: 10px; color: #333; }
  .radio { width: 9px; height: 9px; border: 1px solid #aaa; border-radius: 50%; background: #f4f4f4; }
  .radio.checked { background: radial-gradient(#2a6f9a 35%, #f4f4f4 40%); }
  .select { left: 563px; top: 974px; width: 191px; height: 24px; border: 1px solid #ccc; background: #fafafa; box-shadow: 0 1px 2px rgba(0,0,0,0.15); font-size: 10px; line-height: 22px; padding-left: 9px; color: #444; }
  .select-arrow { position: absolute; right: -1px; top: -1px; width: 23px; height: 24px; background: #3a3a3a; }
  .select-arrow::after { content: ""; position: absolute; left: 6px; top: 10px; border: 5px solid transparent; border-top: 5px solid var(--white); }
  .btn-cart { left: 561px; top: 1022px; width: 139px; height: 29px; background: linear-gradient(#ee4048, #d4262f); font-size: 14px; line-height: 29px; display: flex; align-items: center; justify-content: center; gap: 7px; }

  /* Testimonial */
  .testimonial { left: 0; top: 1098px; width: 896px; height: 65px; background: var(--quote-band); }
  .quote-mark { left: 105px; top: 1098px; width: 22px; height: 65px; background: var(--red); color: var(--white); font-family: "Lora", serif; font-size: 30px; text-align: center; line-height: 70px; }
  .quote-text { left: 138px; top: 1106px; width: 580px; font-family: "Lora", serif; font-style: italic; font-size: 10px; line-height: 15.5px; color: #333; }
  .quote-text cite { display: block; color: var(--red); font-style: italic; margin-top: 2px; }
  .social { top: 1117px; width: 28px; height: 28px; border-radius: 50%; }
  .social.fb { left: 718px; background: var(--fb); }
  .social.tw { left: 752px; background: var(--tw); }

  /* Footer */
  .site-footer { left: 0; top: 1163px; width: 896px; height: 37px; background: var(--footer); color: #ddd; font-size: 10px; line-height: 35px; }
  .footer-nav { position: absolute; left: 105px; }
  .footer-nav a { color: #ddd; text-decoration: none; }
  .footer-nav .sep { margin: 0 5px; }
  .copyright { position: absolute; right: 106px; }
</style>
</head>
<body>

<header class="site-header">
  <svg class="header-glow" width="896" height="457" aria-hidden="true">
    <polygon points="390,0 470,0 330,130 250,130" fill="#141414"/>
    <polygon points="470,0 560,0 430,120 340,120" fill="#1b1b1b"/>
    <polygon points="560,0 640,0 540,90 460,90" fill="#111"/>
    <polygon points="640,0 700,0 630,60 570,60" fill="#161616"/>
  </svg>
</header>

<div class="abs brand"><span class="brand-dot"></span>Velqora</div>
<div class="abs contact-line"><em>Any Questions?</em><strong>123 4670 219</strong></div>

<nav class="abs main-nav">
  <a href="#"><span>HOME</span></a>
  <a href="#"><span>ABOUT</span></a>
  <a href="#"><span>SERVICES</span></a>
  <a href="#"><span>PRODUCT</span></a>
  <a href="#"><span>GALLERY</span></a>
  <a href="#"><span>CONTACT</span></a>
</nav>

<section class="abs hero">
  <div class="hero-inner">
    <div class="hero-photo" role="img" aria-label="Home theatre speaker system with tall tower speakers and a centre unit"></div>
    <h1 class="hero-title">Audio Visual &amp; Security<br>System Installations</h1>
    <p class="hero-copy">This is Draftline's version of Lorem Ipsum. Proin gravida nibh vel velit auctor aliquet. Aenean sollicitudin, lorem quis bibendum auctor, nisi elit consequat ipsum, nec sagittis sem nibh id elit. Duis sed odio sit amet nibh vulputate cursus a sit amet mauris. Morbi accumsan ipsum velit.</p>
    <div class="hero-dots"><i></i><i></i><i></i></div>
  </div>
</section>

<div class="abs services-band"></div>
<article class="abs service-card" style="left:105px">
  <div class="service-photo" role="img" aria-label="Studio microphone, speaker and headphones" style="background:radial-gradient(circle at 55% 45%, #9a9a9a, #e4e4e4 60%, #fff)"></div>
  <div class="service-label">Audio Visual</div>
</article>
<article class="abs service-card" style="left:342px">
  <div class="service-photo" role="img" aria-label="Bundle of gold-plated RCA cables" style="background:radial-gradient(circle at 60% 45%, #b98a3d, #e9dcc2 55%, #fff)"></div>
  <div class="service-label">Data Cabling</div>
</article>
<article class="abs service-card" style="left:579px">
  <div class="service-photo" role="img" aria-label="Wall-mounted white security camera" style="background:radial-gradient(circle at 55% 40%, #c8c8c8, #eee 55%, #fff)"></div>
  <div class="service-label">Security Cameras</div>
</article>

<div class="abs welcome-title"><h2>Welcome to <b>Velqora</b></h2></div>
<div class="abs welcome-copy">
  <p>This is Draftline's version of Lorem Ipsum. Proin gravida nibh vel velit auctor aliquet. Aenean sollicitudin, lorem quis bibendum auctor, nisi elit consequat ipsum, nec sagittis sem nibh id elit. Duis sed odio sit amet nibh vulputate cursus a sit amet mauris. Morbi accumsan ipsum velit. Nam nec tellus a odio tincidunt auctor a ornare odio. Sed non mauris vitae erat consequat auctor eu in elit.</p>
  <p>Class aptent taciti sociosqu ad litora torquent per conubia nostra, per inceptos himenaeos. Mauris in erat justo. Nullam ac urna eu felis dapibus condimentum sit amet a augue. Sed non neque elit. Sed ut imperdiet nisi. Proin condimentum fermentum nunc.</p>
</div>

<section class="abs accessories">
  <h3>DATA CABLING</h3>
  <h2>ACCESSORIES</h2>
  <p>This is Draftline's version of Lorem Ipsum. Proin gravida nibh vel velit auctor aliquet. Aenean sollicitudin, lorem quis bibendum auctor, nisi elit consequat ipsum, nec sagittis sem nibh id elit. Duis sed odio sit amet nibh vulputate cursus a sit amet mauris.</p>
</section>
<a class="abs btn btn-shop" href="#">SHOP NOW!</a>
<div class="abs cables-photo" role="img" aria-label="Fan of colourful network patch cables with RJ45 plugs" style="background:linear-gradient(180deg,#e9d8f3 0%,#d6f1f5 25%,#dff5d8 50%,#fbf3cf 70%,#fde3d3 85%,#fbdada 100%)"></div>
<div class="abs divider"></div>

<section class="abs booking">
  <h2>BOOK ONLINE</h2>
  <ul class="booking-options">
    <li><span class="radio checked"></span>Audio Visual</li>
    <li><span class="radio"></span>Data Cabeling</li>
    <li><span class="radio"></span>CCTV</li>
  </ul>
</section>
<div class="abs select">Select Product<span class="select-arrow"></span></div>
<a class="abs btn btn-cart" href="#">
  <svg width="18" height="15" viewBox="0 0 18 15" aria-hidden="true"><path d="M1 1h3l2 8h9l2-6H5" fill="none" stroke="#fff" stroke-width="1.6"/><circle cx="7" cy="13" r="1.4" fill="#fff"/><circle cx="14" cy="13" r="1.4" fill="#fff"/></svg>
  ADD TO CART
</a>

<div class="abs testimonial"></div>
<div class="abs quote-mark">“</div>
<blockquote class="abs quote-text">“ This is Draftline's version of Lorem Ipsum. Proin gravida nibh vel velit auctor aliquet. Aenean sollicitudin, lorem quis bibendum auctor, nisi elit consequat ipsum, nec sagittis sem nibh id elit. ”<cite>- Client Speak</cite></blockquote>
<a class="abs social fb" href="#" aria-label="Social profile"></a>
<a class="abs social tw" href="#" aria-label="Social profile"></a>

<footer class="abs site-footer">
  <nav class="footer-nav"><a href="#">Home</a><span class="sep">|</span><a href="#">About</a><span class="sep">|</span><a href="#">Services</a><span class="sep">|</span><a href="#">Product</a><span class="sep">|</span><a href="#">Gallery</a><span class="sep">|</span><a href="#">Contact</a></nav>
  <div class="copyright">Copyright ©2013 Velqora. All Rights Reserved.</div>
</footer>

</body>
</html>
```